Vintage Infographic Background Design

I need an infographic which has a vintage background design. The file "Infographic Background Design Primer" describes the nature of the design required. Thank you for taking the time to read this and I look forward to working with you.
Target Market(s)
Law Students
Industry/Entity Type
Law Firm
Font styles to use
Serif
Script
Colors
fece3e
ffcf3e
fbf289
f37122
f04a50
f59195
fee3d4
fbe7d2
fee18a
Requirements
Must have
- All three tasks mentioned in the "Infographic Background Design Primer" uploaded on 20th May 2016.
Should not have
- The infographic should not convey the impression that it is tacky/run of the mill.

```html
<!DOCTYPE html>
<html lang="en">
<head>
<meta charset="utf-8">
<title>Heading / Title</title>
<link rel="stylesheet" href="https://fonts.googleapis.com/css2?family=Great+Vibes&family=Macondo&display=swap">
<style>
  :root {
    --parchment-light: #fbf0a8;
    --parchment-mid: #e8cc78;
    --parchment-deep: #b98d3c;
    --edge-dark: #5a3510;
    --ink: #2b1b12;
    --title-ink: #4a2a1c;
    --rule: rgba(120, 80, 40, 0.35);
    --panel-fill: rgba(251, 242, 137, 0.55);
    --panel-border: rgba(140, 100, 40, 0.55);
    --ornament: rgba(150, 80, 40, 0.35);
    --seal: #9a2c1e;
  }
  html, body {
    margin: 0;
    padding: 0;
    overflow: hidden;
  }
  .sheet {
    position: relative;
    width: 848px;
    height: 1200px;
    overflow: hidden;
    background:
      radial-gradient(ellipse 55% 60% at 52% 42%, var(--parchment-light) 0%, var(--parchment-mid) 45%, var(--parchment-deep) 80%, var(--edge-dark) 100%);
  }
  .sheet::after {
    content: "";
    position: absolute;
    inset: 0;
    background: linear-gradient(90deg, rgba(70,35,10,0.55) 0%, rgba(70,35,10,0) 7%, rgba(70,35,10,0) 93%, rgba(70,35,10,0.55) 100%);
    pointer-events: none;
  }
  .title {
    position: absolute;
    left: 0;
    width: 848px;
    top: 68px;
    margin: 0;
    text-align: center;
    font-family: "Great Vibes", cursive;
    font-weight: 400;
    font-size: 78px;
    line-height: 1;
    color: var(--title-ink);
    letter-spacing: 1px;
  }
  .title-rule {
    position: absolute;
    left: 98px;
    top: 155px;
    width: 652px;
    height: 1px;
    background: var(--rule);
  }
  .topic {
    position: absolute;
    width: 534px;
    height: 131px;
    box-sizing: border-box;
    padding: 14px 18px 0 20px;
    background: var(--panel-fill);
    border: 1px solid var(--panel-border);
    border-radius: 4px;
    font-family: "Macondo", serif;
    font-size: 29px;
    line-height: 34px;
    color: var(--ink);
    margin: 0;
  }
  .topic--first { left: 158px; top: 254px; }
  .topic--second { left: 158px; top: 500px; }
  .topic--third { left: 163px; top: 745px; }
  .footer-ornament {
    position: absolute;
    left: 161px;
    top: 992px;
    width: 530px;
    height: 174px;
  }
  .wax-seal {
    position: absolute;
    left: 697px;
    top: 1055px;
    width: 120px;
    height: 120px;
  }
</style>
</head>
<body>
<main class="sheet">
  <h1 class="title">Heading / Title</h1>
  <div class="title-rule"></div>

  <p class="topic topic--first">subject subject subject topic subject topic brochure font to be used for the topic</p>
  <p class="topic topic--second">subject subject subject topic subject topic brochure font to be used for the topic</p>
  <p class="topic topic--third">subject subject subject topic subject topic brochure font to be used for the topic</p>

  <svg class="footer-ornament" viewBox="0 0 530 174" role="img" aria-label="Faint flourish ornament with a leaf motif">
    <defs>
      <radialGradient id="ornamentGlow" cx="50%" cy="60%" r="55%">
        <stop offset="0%" stop-color="#965028" stop-opacity="0.32"/>
        <stop offset="100%" stop-color="#965028" stop-opacity="0"/>
      </radialGradient>
    </defs>
    <ellipse cx="265" cy="100" rx="265" ry="74" fill="url(#ornamentGlow)"/>
  </svg>

  <svg class="wax-seal" viewBox="0 0 120 120" role="img" aria-label="Red wax seal">
    <circle cx="60" cy="60" r="58" fill="var(--seal)" opacity="0.85"/>
  </svg>
</main>
</body>
</html>
```